Book Cover Design - Rooted Together: 7 Paths to Raise a Home that Flourishes

International cover needed for the Australian (Marlow Fenwick/QRT Press 2011) non-fiction book Rooted Together: 7 Paths to Raise a Home that Flourishes.

Blurb: With the birth of a baby, come other new beginnings, the birth of a mother, of a father, and of a family. With each stage of a child's growth, and with every new baby, there are more new beginnings. In older cultures and in villages around the world, parenthood was considered a rite of passage but traditions that guided parents into becoming a family have largely been lost - until now.

This ground breaking book walks a new generation of mothers and fathers through the eight steps of the modern parenthood rite of passage, from couple-connection to family-foundations, so they can prepare for and continue to grow a family that thrives.

Bio: Mara Quinlan is a relationship counsellor, parent educator and columnist for Sensible Homelife magazine. She lives in Sydney with her husband, their three gorgeous children and an itinerary of pets. This is her first book.
Updates

Thank you for your patience, I haven't ever done anything like this before and the designs submitted have helped me to be more specific in my requests. Please see the updated brief. The most important point is that I am seeking a TEXT based cover, so BOTH the TITLE and SUBTITLE should take up most of the space, the image could either be in the background with the title and subtitle overlayed, or be much smaller to fit around them. I have attached some more images to the brief, hope they help to convey the 'feel' I am after.  Thanks again!

Reason: Thank you so much for taking an interest in this project, the process has been very educational and helpful for me. While some of the stock art in the submitted designs are great, I've decided to commission a custom illustration which completely captures the meaning of Rooted Together. I will upload the illustration once it's complete for designers who are still interested to use. Thank you for your patience! Mara

Thank you all for your patience and for opening up my thinking about what I am really hoping for with this cover. I have uploaded some new tree designs and more specific instructions that I would like to be included in the cover design. I'm looking forward to seeing your creations!

With warm regards,

Mara

Target Market(s)

Couples thinking about having a baby and new parents of one or more young children.

Industry/Entity Type

Baby

Requirements
Must have
• TEXT based cover with BOTH the TITLE and SUBTITLE taking up most of the page.
Colors to match the Australian version (see attached)
Tree design bottom left (as per Trunk Treatment image attached) OR Heart Tree Design
Root design (as per one of the two images attached)
PLEASE ADD: three new shoots coming up from the ground under the tree to symbolize the children.
Nice to have
• Artistic effect to complement Australian cover.
Subtle retro feel to complement Australian cover.
Should not have
• The book is inclusive of all parents (including same-sex parents) so no images of mother/father and baby.

```html
<!DOCTYPE html>
<html lang="en">
<head>
<meta charset="utf-8">
<title>Rooted Together – Book Cover Wrap</title>
<link href="https://fonts.googleapis.com/css2?family=Pacifico&family=Oswald:wght@300&family=Crimson+Text:ital@0;1&display=swap" rel="stylesheet">
<style>
  :root {
    --backdrop: #f3efd9;
    --paper: #fefdd8;
    --blue: #27a2da;
    --orange: #cf6e1d;
    --green: #6fbf3e;
    --body-green: #74b04a;
    --shadow: rgba(90, 80, 40, 0.35);
  }
  * { margin: 0; padding: 0; box-sizing: border-box; }
  html, body {
    width: 1200px; height: 900px; overflow: hidden;
    background: var(--backdrop);
  }
  .cover-wrap {
    position: absolute; left: 87px; top: 85px;
    width: 1028px; height: 730px;
    background: var(--paper);
    box-shadow: 4px 6px 14px var(--shadow);
  }
  .script { font-family: "Pacifico", cursive; font-weight: 400; }
  .condensed { font-family: "Oswald", sans-serif; font-weight: 300; text-transform: uppercase; }
  .serif { font-family: "Crimson Text", serif; }

  /* Back cover */
  .back {
    position: absolute; left: 0; top: 0; width: 462px; height: 100%;
    text-align: center;
  }
  .back-sprig {
    position: absolute; left: 128px; top: 50px; width: 220px; height: 85px;
    border-radius: 110px 110px 40px 40px;
    background: radial-gradient(ellipse at 50% 70%, rgba(240,80,138,.35), rgba(60,184,200,.28) 45%, rgba(111,191,62,.2) 70%, transparent 75%);
  }
  .back-copy {
    position: absolute; left: 0; top: 135px; width: 100%;
    display: flex; flex-direction: column; align-items: center;
  }
  .back-title {
    color: var(--blue); font-size: 42px; line-height: 58px;
  }
  .back-subtitle {
    color: var(--orange); font-size: 21px; line-height: 28px; letter-spacing: .5px;
    margin-bottom: 8px;
  }
  .blurb {
    color: var(--body-green);
    font-size: 14.5px; line-height: 18px;
  }
  .blurb-one { width: 400px; }
  .blurb-two { width: 270px; margin-top: 16px; }
  .bio {
    width: 150px; margin-top: 16px;
    color: var(--orange); font-size: 14.5px; line-height: 18px;
  }
  .bio .author-name { font-family: "Pacifico", cursive; font-size: 15px; }

  /* Spine */
  .spine {
    position: absolute; left: 462px; top: 0; width: 80px; height: 100%;
  }
  .spine-title {
    position: absolute; left: 24px; top: 42px;
    writing-mode: vertical-rl; white-space: nowrap;
    color: var(--blue); line-height: 32px;
  }
  .spine-title .script { font-size: 21px; }
  .spine-title .condensed { font-size: 16px; margin-top: 10px; }
  .spine-author {
    position: absolute; left: 24px; top: 575px;
    writing-mode: vertical-rl; white-space: nowrap;
    color: var(--green); font-size: 20px; line-height: 32px;
  }

  /* Front cover */
  .front {
    position: absolute; left: 542px; top: 0; width: 486px; height: 100%;
    text-align: center;
  }
  .heart-tree {
    position: absolute; left: 33px; top: 10px; width: 432px; height: 418px;
    border-radius: 50%;
    background:
      radial-gradient(circle at 50% 45%, rgba(240,80,138,.32), rgba(60,184,200,.26) 40%, rgba(111,191,62,.24) 62%, rgba(207,110,29,.18) 72%, transparent 74%);
  }
  .front-title {
    position: absolute; left: 0; width: 100%; top: 120px;
    color: var(--blue); line-height: 1;
  }
  .front-title .line-one { display: block; font-size: 78px; line-height: 98px; }
  .front-title .line-two { display: block; font-size: 78px; line-height: 98px; }
  .front-subtitle {
    position: absolute; left: 0; width: 100%; top: 446px;
    color: var(--orange); font-size: 40px; line-height: 44px; letter-spacing: 1px;
  }
  .front-author {
    position: absolute; left: 0; width: 100%; top: 630px;
    color: var(--green); font-size: 27px; line-height: 44px; letter-spacing: 1px;
    font-family: "Pacifico", cursive; text-transform: uppercase;
  }
  .ground-line { position: absolute; left: 0; top: 655px; width: 486px; height: 40px; }
</style>
</head>
<body>
  <main class="cover-wrap">
    <section class="back">
      <div class="back-sprig" role="img" aria-label="Small fan of colourful hand-drawn leaves, flowers and hearts"></div>
      <div class="back-copy">
        <h2 class="back-title script">Rooted Together</h2>
        <p class="back-subtitle condensed">7 Paths to Raise a Home that Flourishes</p>
        <p class="blurb blurb-one serif">With the birth of a baby, come other new beginnings, the birth of a mother, of a father, and of a family. With each stage of a child’s growth, and with every new baby, there are more new beginnings. In older cultures and in villages around the world, parenthood was considered a rite of passage but traditions that guided parents into becoming a family have largely been lost – until now.</p>
        <p class="blurb blurb-two serif">This ground breaking book walks a new generation of mothers and fathers through the eight steps of the modern parenthood rite of passage, from couple-connection to family-foundations, so they can prepare for and continue to grow a family that thrives.</p>
        <p class="bio serif"><span class="author-name">Mara Quinlan</span> is a relationship counsellor, parent educator and columnist for Sensible Homelife magazine. She lives in Sydney with her husband, their three gorgeous children and an itinerary of pets. This is her first book.</p>
      </div>
    </section>

    <section class="spine">
      <div class="spine-title"><span class="script">Rooted Together</span> <span class="condensed">7 Paths to Raise a Home that Flourishes</span></div>
      <div class="spine-author script">Mara Quinlan</div>
    </section>

    <section class="front">
      <div class="heart-tree" role="img" aria-label="Round tree crown of colourful hand-drawn hearts, leaves, flowers and branches"></div>
      <h1 class="front-title script"><span class="line-one">Rooted</span><span class="line-two">Together</span></h1>
      <p class="front-subtitle condensed">7 Paths<br>to Raise<br>a Home that<br>Flourishes</p>
      <p class="front-author">Mara Quinlan</p>
      <svg class="ground-line" viewBox="0 0 486 40" aria-hidden="true">
        <path d="M4 26 C20 18 30 30 46 24 C66 18 80 28 98 27 M390 27 C405 25 412 18 428 23 C446 29 462 22 484 24"
              fill="none" stroke="var(--green)" stroke-width="3" stroke-linecap="round"/>
      </svg>
    </section>
  </main>
</body>
</html>
```